Automotive Parts Company Business Card/Logo Design

We need a logo/business card for a new automotive parts and accessories company which is based in Barbados. The company will only have an online presence and this will reduce our overheads and allow us to pass potential savings to our customers.

We will offer most automotive parts which include, but are not limited to, accessories, exterior, interior, body parts.

We want to appeal to a very wide audience and we're looking for a modern, clean and bold design to make the company seem very professional. Our logo and facebook page will be our only customer facing items. So it is essential that these are done correctly.

The design should really communicate that we can provide premium car parts at affordable prices for all types of cars e.g. European and Japanese.

We will stock items and also source hard to get and unique pieces. We aim to not just be another shop that sells parts. But we want to work with our customers to achieve their car goals.

The company name is GearVista and our slogan is Quality Parts At Affordable Prices.
The design should be very modern, clean and bold.

I've included examples of some of the business cards I like as well as images of car products.
Updates

Dear Designers,

I've uploaded some samples of some business card/logo designs I like. Please have a look at the project brief. Just to reiterate, I am looking for a clean, modern design.

Thanks,

Rohan

Dear Designers,

Please note the Apr 14th deadline is soon approaching.

Also note the business card is double-sided.

I look forward to working with you.

Thanks,

Rohan

Target Market(s)

20 - 30 (young professionals, younger generation with disposible income) and then then all other markets

Industry/Entity Type

Automotive

Contact Information for Business Card

Rohan Melwanikar
GearVista
Quality Parts At Affordable Prices
https://www.examplesocial.test/gearvistabq
246-319-8042
gearvistabq@mailbox-example.test

```html
<!DOCTYPE html>
<html lang="en">
<head>
<meta charset="utf-8">
<title>GearVista Business Card</title>
<link href="https://fonts.googleapis.com/css2?family=Oswald:wght@400;500&family=Roboto+Condensed:wght@400&display=swap" rel="stylesheet">
<style>
  :root {
    --page: #e9e7e4;
    --card-dark: #3b3b3d;
    --card-darker: #232325;
    --stripe: rgba(255,255,255,0.09);
    --lime: #a4cc2d;
    --white: #ffffff;
    --grey-text: #6d6e70;
    --bar-dark: #3a3a3c;
    --bar-light: #8a8a8c;
  }
  * { margin: 0; padding: 0; box-sizing: border-box; }
  html, body { width: 1200px; height: 900px; overflow: hidden; background: var(--page); }
  .canvas {
    width: 1200px; height: 900px; position: relative;
    display: flex; flex-direction: column; align-items: center; justify-content: center; gap: 40px;
  }
  .card {
    width: 700px; height: 400px; border-radius: 22px; position: relative; overflow: hidden;
    box-shadow: 0 14px 30px rgba(0,0,0,0.22);
  }

  /* Front */
  .card-front {
    background:
      repeating-linear-gradient(160deg, transparent 0 44px, var(--stripe) 44px 46px),
      linear-gradient(180deg, var(--card-dark), var(--card-darker));
  }
  .photo-strip { position: absolute; left: 0; right: 0; top: 36px; height: 175px; display: flex; }
  .photo { height: 100%; }
  .photo-car-silver { width: 36%; background: linear-gradient(135deg, #9fa2a6, #5d6166 60%, #4a4238); }
  .photo-wheels { width: 32%; background: linear-gradient(180deg, #f1f1f1, #d9d9db 55%, #bdbdbf); }
  .photo-car-orange { width: 32%; background: linear-gradient(135deg, #c8c2b4, #ef7a22 55%, #3e3f44); }
  .brand { position: absolute; right: 34px; top: 214px; text-align: right; }
  .brand-name {
    font-family: "Oswald", sans-serif; font-weight: 500; font-size: 80px; line-height: 1;
    color: var(--white); letter-spacing: 1px; text-transform: uppercase;
  }
  .slogan {
    font-family: "Oswald", sans-serif; font-weight: 400; font-size: 26px; color: var(--white);
    margin-top: 6px;
  }

  /* Back */
  .card-back { background: var(--white); }
  .flag-band { position: absolute; inset: 0; }
  .contact-list { position: absolute; left: 0; top: 132px; width: 370px; list-style: none; }
  .contact-row {
    height: 40px; display: flex; align-items: center; justify-content: flex-end;
    border-bottom: 3px solid var(--white);
    background: linear-gradient(90deg, rgba(58,58,60,0) 0%, var(--bar-dark) 70%);
  }
  .contact-row:nth-child(2) { background: linear-gradient(90deg, rgba(138,138,140,0) 0%, var(--bar-light) 70%); }
  .contact-text {
    font-family: "Roboto Condensed", sans-serif; font-size: 15px; color: var(--white);
    padding-right: 10px; white-space: nowrap;
  }
  .contact-icon {
    width: 40px; height: 40px; flex: none; display: flex; align-items: center; justify-content: center;
    border-left: 2px solid var(--white); background: var(--bar-light);
  }
  .name { position: absolute; left: 386px; top: 118px; font-family: "Oswald", sans-serif; text-transform: uppercase; line-height: 0.98; }
  .name-first { color: var(--lime); font-weight: 500; font-size: 52px; }
  .name-last { color: var(--grey-text); font-weight: 400; font-size: 44px; }
</style>
</head>
<body>
<main class="canvas">
  <section class="card card-front" aria-label="Business card front">
    <div class="photo-strip">
      <div class="photo photo-car-silver" role="img" aria-label="Photo of a silver tuned sports car"></div>
      <div class="photo photo-wheels" role="img" aria-label="Photo of alloy wheels on a display wall"></div>
      <div class="photo photo-car-orange" role="img" aria-label="Photo of an orange and black performance car"></div>
    </div>
    <div class="brand">
      <h1 class="brand-name">GearVista</h1>
      <p class="slogan">Quality Parts At Affordable Prices</p>
    </div>
  </section>

  <section class="card card-back" aria-label="Business card back">
    <svg class="flag-band" width="700" height="400" viewBox="0 0 700 400" role="img" aria-label="Waving chequered racing flag band">
      <defs>
        <linearGradient id="flagTone" x1="0" y1="1" x2="1" y2="0">
          <stop offset="0" stop-color="#1d1d1f"/>
          <stop offset="0.5" stop-color="#6a6a6c"/>
          <stop offset="1" stop-color="#1d1d1f"/>
        </linearGradient>
      </defs>
      <path d="M 300 400 C 380 330, 430 300, 520 285 C 600 272, 650 250, 700 210 L 700 290 C 650 320, 600 335, 530 345 C 460 356, 420 375, 390 400 Z" fill="url(#flagTone)"/>
    </svg>

    <ul class="contact-list">
      <li class="contact-row">
        <span class="contact-text">246-319-8042</span>
        <span class="contact-icon">
          <svg width="18" height="18" viewBox="0 0 24 24" aria-hidden="true"><path fill="#fff" d="M6.6 10.8a15 15 0 0 0 6.6 6.6l2.2-2.2c.3-.3.7-.4 1-.2 1.1.4 2.3.6 3.6.6.6 0 1 .4 1 1V20c0 .6-.4 1-1 1A17 17 0 0 1 3 4c0-.6.4-1 1-1h3.5c.6 0 1 .4 1 1 0 1.3.2 2.5.6 3.6.1.3 0 .7-.2 1z"/></svg>
        </span>
      </li>
      <li class="contact-row">
        <span class="contact-text">gearvistabq@mailbox-example.test</span>
        <span class="contact-icon">
          <svg width="20" height="16" viewBox="0 0 20 16" aria-hidden="true"><rect x="1" y="1" width="18" height="14" fill="none" stroke="#fff" stroke-width="2"/><path d="M1 1 L10 9 L19 1" fill="none" stroke="#fff" stroke-width="2"/></svg>
        </span>
      </li>
      <li class="contact-row">
        <span class="contact-text">https://www.examplesocial.test/gearvistabq</span>
        <span class="contact-icon">
          <svg width="14" height="14" viewBox="0 0 14 14" aria-hidden="true"><rect width="14" height="14" fill="#fff"/></svg>
        </span>
      </li>
    </ul>

    <div class="name">
      <p class="name-first">Rohan</p>
      <p class="name-last">Melwanikar</p>
    </div>
  </section>
</main>
</body>
</html>
```